Single brochure for international companies in the financial sector

We need to update a brochure 4 pages presenting our company. We are a financial engineering company. The final design must provide financial security, service and trust. you will find the current brochure copy. Our color code is Orange (RGB 235/100/68), Black, White and Gray. photos show the visual of the site, but it is not mandatory to keep them.

Target Market(s)

wealth management professionals

Industry/Entity Type

Finance

Requirements
Must have
• Logo Velbrook Capital all text in the document color Orange Velbrook (RGB 235/100/68)
Nice to have
• Vista Font
Should not have
• images / pictures of people

```html
<!DOCTYPE html>
<html lang="en">
<head>
<meta charset="utf-8">
<title>Velbrook Capital – Brochure Covers</title>
<link href="https://fonts.googleapis.com/css2?family=Jost:wght@400;500&display=swap" rel="stylesheet">
<style>
  :root {
    --orange: #eb6444;
    --navy: #2f3d54;
    --navy-deep: #243146;
    --paper: #ffffff;
    --paper-shade: #ececec;
    --ground: #e4e4e4;
    --ink-grey: #6b6f78;
    --sky: #2f7fc6;
    --sea: #2d6f86;
  }
  html, body {
    margin: 0;
    padding: 0;
    width: 874px;
    height: 1200px;
    overflow: hidden;
    background: var(--ground);
    font-family: "Jost", "Helvetica Neue", Arial, sans-serif;
  }
  .sheet {
    position: relative;
    width: 874px;
    height: 1200px;
  }
  .page {
    position: absolute;
    left: 237px;
    width: 400px;
    height: 566px;
    box-shadow: 0 6px 18px rgba(0,0,0,0.18);
    background: var(--paper);
  }
  .page--front { top: 24px; }
  .page--back  { top: 610px; }
  .page svg { display: block; width: 400px; height: 566px; }
  .logo-name { font-size: 19px; letter-spacing: 9px; fill: var(--orange); font-weight: 400; }
  .logo-sub  { font-size: 10px; letter-spacing: 5px; fill: var(--orange); font-weight: 400; }
  .cover-title { font-size: 21px; fill: #ffffff; font-weight: 400; letter-spacing: 0.5px; }
  .web { font-size: 8px; letter-spacing: 2.6px; fill: var(--ink-grey); }
  .contact { font-size: 8px; fill: #ffffff; }
  .contact--strong { font-weight: 500; }
  .icon { fill: var(--orange); }
</style>
</head>
<body>
<div class="sheet">

  <!-- Front cover -->
  <section class="page page--front">
    <svg viewBox="0 0 400 566" xmlns="http://www.w3.org/2000/svg">
      <defs>
        <linearGradient id="paperFront" x1="0" y1="0" x2="1" y2="0">
          <stop offset="0" stop-color="var(--paper-shade)"/>
          <stop offset="0.6" stop-color="var(--paper)"/>
        </linearGradient>
        <linearGradient id="coverScene" x1="0" y1="0" x2="0" y2="1">
          <stop offset="0" stop-color="#1f5fae"/>
          <stop offset="0.4" stop-color="var(--sky)"/>
          <stop offset="0.75" stop-color="var(--sea)"/>
          <stop offset="1" stop-color="#26586a"/>
        </linearGradient>
      </defs>
      <rect width="400" height="566" fill="url(#paperFront)"/>

      <g class="brand">
        <text class="logo-name" x="34" y="118">VELBROOK</text>
        <text class="logo-sub" x="78" y="136">CAPITAL</text>
      </g>

      <path d="M0,208 C130,185 300,115 400,22" fill="none" stroke="var(--orange)" stroke-width="3"/>
      <path class="cover-photo" role="img" aria-label="Photo of a red suspension bridge over a bay under a blue sky"
            d="M0,222 C130,200 300,130 400,40 L400,392 C290,382 130,395 0,440 Z" fill="url(#coverScene)"/>
      <path d="M0,452 C130,410 290,395 400,404" fill="none" stroke="var(--orange)" stroke-width="3"/>

      <text class="cover-title" x="378" y="332" text-anchor="end">FINANCIAL</text>
      <text class="cover-title" x="378" y="358" text-anchor="end">ENGINEERING</text>

      <text class="web" x="370" y="540" text-anchor="end">www.velbrookcapital.com</text>
    </svg>
  </section>

  <!-- Back cover -->
  <section class="page page--back">
    <svg viewBox="0 0 400 566" xmlns="http://www.w3.org/2000/svg">
      <defs>
        <linearGradient id="backScene" x1="0" y1="0" x2="0" y2="1">
          <stop offset="0" stop-color="var(--navy)"/>
          <stop offset="1" stop-color="var(--navy-deep)"/>
        </linearGradient>
      </defs>
      <rect width="400" height="566" fill="var(--paper)"/>

      <path d="M140,136 C240,128 330,125 400,118" fill="none" stroke="var(--orange)" stroke-width="2.5"/>
      <path class="back-photo" role="img" aria-label="Faint photo of an iron tower under a cloudy sky, tinted navy"
            d="M0,142 C140,140 280,134 400,126 L400,352 C270,372 120,430 0,520 Z" fill="url(#backScene)"/>
      <path d="M0,534 C120,444 270,386 400,366" fill="none" stroke="var(--orange)" stroke-width="3"/>

      <g class="contact-block" text-anchor="middle">
        <text class="logo-name" x="200" y="200" style="font-size:14px;letter-spacing:7px">VELBROOK</text>
        <text class="logo-sub" x="200" y="214" style="font-size:8px;letter-spacing:4px">CAPITAL</text>
        <text class="contact contact--strong" x="200" y="230">CODE BANQUE (CIB) : 10472</text>

        <path class="icon" d="M200,238 a4,4 0 0 1 4,4 c0,3 -4,7 -4,7 s-4,-4 -4,-7 a4,4 0 0 1 4,-4 z"/>
        <text class="contact" x="200" y="261">Velbrook Capital SA, Capital :</text>
        <text class="contact" x="200" y="271">400 000 Euros</text>
        <text class="contact" x="200" y="281">RCS Paris : 812 456 903</text>

        <path class="icon" d="M196,290 l2,-1 l2,3 l-1,1 c1,2 2,3 4,4 l1,-1 l3,2 l-1,2 c-5,0 -10,-5 -10,-10 z"/>
        <text class="contact" x="200" y="310">+33 1 40 00 12 34</text>

        <rect class="icon" x="195" y="318" width="10" height="7"/>
        <path d="M195,318 l5,4 l5,-4" fill="none" stroke="var(--navy)" stroke-width="0.8"/>
        <text class="contact" x="200" y="337">contact@velbrookcapital.com</text>
      </g>

      <text class="web" x="200" y="548" text-anchor="middle">www.velbrookcapital.com</text>
    </svg>
  </section>

</div>
</body>
</html>
```